Korimet Business Cards

Korimet is a software startup and we are looking for business cards that help convey our employee personalities, as well as the professionalism of the company.
Our company font is Comfortaa - and the company logo is attached (we are okay having the text beside the logo if applicable) where we can find the company colour scheme. Cards can be horizontal or vertical format.
We are looking for a two sided business card - on the front we will see the personal details of the employee (name, position, email and phone number), and then on the back, we will see the business details (name and logo, address, phone number, website, email, company tagline: "Accelerating technology disruption in the automotive market")
We want the design to be clean and simple, but also fun, modern, and capturing of a young startup vibe.

```html
<!DOCTYPE html>
<html lang="en">
<head>
<meta charset="utf-8">
<title>Korimet Business Cards</title>
<link href="https://fonts.googleapis.com/css2?family=Comfortaa:wght@400;600;700&display=swap" rel="stylesheet">
<style>
  :root {
    --stage: #1e1e20;
    --card-dark: #272729;
    --card-light: #f7f6f8;
    --violet: #5a3fce;
    --magenta: #c54cc3;
    --ink-light: #d8d8dc;
    --ink-dark: #555559;
  }
  * { box-sizing: border-box; margin: 0; padding: 0; }
  html, body {
    width: 1200px; height: 874px; overflow: hidden;
    background: var(--stage);
    font-family: "Comfortaa", sans-serif;
  }
  .stage {
    position: relative; width: 1200px; height: 874px;
    display: flex; justify-content: center; align-items: center; gap: 70px;
  }
  .card {
    width: 440px; height: 770px; border-radius: 30px;
    display: flex; flex-direction: column; align-items: center;
    padding: 120px 40px 70px; text-align: center;
  }
  .card--front { background: var(--card-light); }
  .card--back { background: var(--card-dark); }
  .wordmark {
    display: flex; align-items: center; gap: 16px;
    font-weight: 700; font-size: 60px; color: var(--violet);
    letter-spacing: 1px;
  }
  .wordmark__dot {
    width: 26px; height: 26px; border-radius: 50%; background: var(--violet);
  }
  .person__name {
    margin-top: 90px; font-size: 34px; font-weight: 700;
    color: var(--violet); letter-spacing: 1px;
  }
  .person__role { margin-top: 8px; font-size: 22px; color: var(--magenta); }
  .icon-row {
    display: flex; align-items: center; gap: 10px; margin-top: 34px;
  }
  .icon-row__rule { width: 18px; height: 2px; }
  .icon-row svg { width: 40px; height: 40px; display: block; }
  .card--front .icon-row__rule { background: var(--magenta); }
  .card--back .icon-row__rule { background: var(--violet); }
  .contact {
    margin-top: 36px; font-size: 22px; line-height: 1.45;
  }
  .card--front .contact { color: var(--ink-dark); }
  .card--back .contact { color: var(--ink-light); }
  .contact + .contact { margin-top: 26px; }
  .tagline {
    margin-top: auto; font-size: 19px; line-height: 1.35; color: var(--magenta);
  }
  .tagline__strong { display: block; font-size: 22px; text-transform: uppercase; }
</style>
</head>
<body>
<main class="stage">

  <section class="card card--front" aria-label="Front of card">
    <div class="wordmark"><span class="wordmark__dot"></span>korimet</div>
    <h1 class="person__name">DANIEL REYES</h1>
    <p class="person__role">President</p>
    <div class="icon-row">
      <span class="icon-row__rule"></span>
      <svg viewBox="0 0 40 40" aria-label="mobile">
        <circle cx="20" cy="20" r="17" fill="none" stroke="var(--violet)" stroke-width="3"/>
        <rect x="14" y="11" width="12" height="18" rx="2" fill="none" stroke="var(--violet)" stroke-width="2.5"/>
      </svg>
      <svg viewBox="0 0 40 40" aria-label="email">
        <circle cx="20" cy="20" r="17" fill="none" stroke="var(--violet)" stroke-width="3"/>
        <rect x="11" y="14" width="18" height="12" rx="1" fill="var(--violet)"/>
        <path d="M11 14 L20 21 L29 14" fill="none" stroke="var(--card-light)" stroke-width="1.6"/>
      </svg>
      <span class="icon-row__rule"></span>
    </div>
    <p class="contact">daniel@korimet.com<br>555-018-4471</p>
  </section>

  <section class="card card--back" aria-label="Back of card">
    <div class="wordmark"><span class="wordmark__dot"></span>korimet</div>
    <div class="icon-row" style="margin-top:60px">
      <span class="icon-row__rule"></span>
      <svg viewBox="0 0 40 40" aria-label="location">
        <circle cx="20" cy="20" r="17" fill="none" stroke="var(--magenta)" stroke-width="3"/>
        <path d="M20 29 C15 23 14 20 14 17 a6 6 0 0 1 12 0 c0 3 -1 6 -6 12z" fill="var(--magenta)"/>
        <circle cx="20" cy="17" r="2.2" fill="var(--card-dark)"/>
      </svg>
      <svg viewBox="0 0 40 40" aria-label="phone">
        <circle cx="20" cy="20" r="17" fill="none" stroke="var(--magenta)" stroke-width="3"/>
        <path d="M15 12 l3 0 l1.5 4 l-2 1.5 c1 2.5 2.5 4 5 5 l1.5 -2 l4 1.5 l0 3 c-8 1 -14 -5 -13 -13z" fill="var(--magenta)"/>
      </svg>
      <svg viewBox="0 0 40 40" aria-label="email">
        <circle cx="20" cy="20" r="17" fill="none" stroke="var(--magenta)" stroke-width="3"/>
        <rect x="11" y="14" width="18" height="12" rx="1" fill="var(--magenta)"/>
        <path d="M11 14 L20 21 L29 14" fill="none" stroke="var(--card-dark)" stroke-width="1.6"/>
      </svg>
      <svg viewBox="0 0 40 40" aria-label="website">
        <circle cx="20" cy="20" r="17" fill="none" stroke="var(--magenta)" stroke-width="3"/>
        <circle cx="20" cy="20" r="8" fill="var(--magenta)"/>
        <path d="M12 20 h16 M20 12 c-4 5 -4 11 0 16 M20 12 c4 5 4 11 0 16" fill="none" stroke="var(--card-dark)" stroke-width="1.4"/>
      </svg>
      <span class="icon-row__rule"></span>
    </div>
    <p class="contact">4120 Willow Bend Road<br>Fairbanks, Alaska 34210</p>
    <p class="contact">555-014-2237<br>info@korimet.com<br>www.korimet.com</p>
    <p class="tagline">Accelerating technology disruption in
      <span class="tagline__strong">the automotive market</span></p>
  </section>

</main>
</body>
</html>
```